Stationary design for IT Consultancy
Stationary Design (Business Cards - Letter Heads - Envelopes - Presentation Folders - Power Point)
Stationary design for IT Consultancy - Information Technology
Creative Brief
Use standard fonts
Optional fonts can be used
Professional
Dean Marlow
Technical Director
14 Brindle Works Oakfield Lane Stoneham Wexshire WX7 2QP
dean.marlow@pivotal-nsg.net
www.pivotal-nsg.net

```html
<!DOCTYPE html>
<html lang="en">
<head>
<meta charset="utf-8">
<title>Pivotal Network Systems Group – Business Card</title>
<link href="https://fonts.googleapis.com/css2?family=Michroma&display=swap" rel="stylesheet">
<style>
  :root {
    --brand-blue: #3d5cc4;
    --brand-blue-deep: #2f4aa8;
    --brand-blue-light: #8fa3e0;
    --card-white: #fbfbfd;
    --stage: #e9eaee;
    --ink-muted: #6d7aa8;
  }
  * { box-sizing: border-box; margin: 0; padding: 0; }
  html, body {
    width: 1200px; height: 991px; overflow: hidden;
    background: var(--stage);
    font-family: "Michroma", sans-serif;
  }
  .canvas { position: relative; width: 1200px; height: 991px; }
  .card {
    position: absolute; left: 290px; width: 620px; height: 400px;
    overflow: hidden; border-radius: 3px;
    box-shadow: 0 6px 18px rgba(30,40,80,.18);
  }
  .card--back { top: 70px; background: var(--brand-blue); }
  .card--front { top: 521px; background: var(--card-white); }

  .brand { position: absolute; text-align: left; }
  .brand__name { font-size: 46px; letter-spacing: 3px; line-height: 1; }
  .brand__tag { font-size: 13px; letter-spacing: 4.6px; margin-top: 8px; }
  .card--back .brand { left: 50%; top: 150px; transform: translateX(-50%); color: #fff; }
  .card--front .brand { left: 150px; top: 58px; color: var(--brand-blue); }

  .wave { position: absolute; inset: 0; width: 620px; height: 400px; }

  .person { position: absolute; right: 32px; top: 176px; text-align: right; color: var(--brand-blue); }
  .person__name { font-size: 12px; letter-spacing: 1.5px; }
  .person__role { font-size: 8px; letter-spacing: 1.5px; margin-top: 5px; color: var(--ink-muted); }

  .address {
    position: absolute; left: 40px; top: 292px; width: 250px;
    color: #fff; font-size: 8.5px; line-height: 1.8; letter-spacing: .8px;
  }
  .contact { position: absolute; left: 360px; top: 282px; list-style: none; color: #fff; }
  .contact li {
    display: flex; align-items: center; gap: 9px;
    font-size: 8.5px; letter-spacing: .6px; height: 20px;
  }
  .contact svg { width: 12px; height: 12px; flex: none; }
</style>
</head>
<body>
<main class="canvas">

  <section class="card card--back" aria-label="Business card back">
    <div class="brand">
      <div class="brand__name">PIVOTAL</div>
      <div class="brand__tag">NETWORK SYSTEMS GROUP</div>
    </div>
  </section>

  <section class="card card--front" aria-label="Business card front">
    <svg class="wave" viewBox="0 0 620 400" aria-hidden="true">
      <path d="M0 232 C200 272 420 262 620 196 L620 400 L0 400 Z" fill="var(--brand-blue-light)" opacity=".45"/>
      <path d="M0 246 C210 286 430 276 620 212 L620 400 L0 400 Z" fill="var(--brand-blue)"/>
      <path d="M0 262 C220 300 440 290 620 230" fill="none" stroke="#fff" stroke-width="1.4" opacity=".7"/>
    </svg>

    <div class="brand">
      <div class="brand__name">PIVOTAL</div>
      <div class="brand__tag">NETWORK SYSTEMS GROUP</div>
    </div>

    <div class="person">
      <div class="person__name">DEAN MARLOW</div>
      <div class="person__role">TECHNICAL DIRECTOR</div>
    </div>

    <address class="address" style="font-style:normal">
      14 Brindle Works Oakfield Lane<br>
      Stoneham Wexshire WX7 2QP
    </address>

    <ul class="contact">
      <li>
        <svg viewBox="0 0 12 12"><circle cx="6" cy="6" r="6" fill="#fff"/><path d="M4 3.2l1 1.6-.6.7c.4.9 1.1 1.6 2 2l.7-.6 1.6 1-.5 1c-2.4-.1-4.4-2.1-4.6-4.6z" fill="var(--brand-blue)"/></svg>
        +44 (0) 1632 960 418
      </li>
      <li>
        <svg viewBox="0 0 12 12"><circle cx="6" cy="6" r="6" fill="#fff"/><rect x="3" y="4" width="6" height="4.2" fill="none" stroke="var(--brand-blue)" stroke-width=".9"/><path d="M3 4l3 2.3L9 4" fill="none" stroke="var(--brand-blue)" stroke-width=".9"/></svg>
        dean.marlow@pivotal-nsg.net
      </li>
      <li>
        <svg viewBox="0 0 12 12"><circle cx="6" cy="6" r="6" fill="#fff"/><circle cx="6" cy="6" r="3.2" fill="none" stroke="var(--brand-blue)" stroke-width=".8"/><path d="M2.8 6h6.4M6 2.8c-1.6 1.8-1.6 4.6 0 6.4M6 2.8c1.6 1.8 1.6 4.6 0 6.4" fill="none" stroke="var(--brand-blue)" stroke-width=".7"/></svg>
        www.pivotal-nsg.net
      </li>
    </ul>
  </section>

</main>
</body>
</html>
```